Unique, Impressive, and Modern Business Card

Looking for a distinctive, unique business card. We are distributors of tire repairs supplies, tools, machinery, and chemicals. Our target market are tire repair shops, tire franchises, and mechanic shops. We would like our design to include tire characteristics, and use our business colors. Feel free to use all types design and printing options (emboss, spot uv, foil, etc) QR code may be applied, you can use different size business cards ( standard, square, rounded edge, colored edge, etc), all formats needed for printing, also editable for future changes

Target Market(s)

Automotive, Tire industries

Industry/Entity Type

Tire Industry (automotive)

Contact Information for Business Card

Business logo, business Name (Corvane Supply Inc), Name (Marcus Pellow), Position (President) Address (58 Fernhollow Lane, Brentwood NY 11742), Contact number (Company 1-855-302-4418, Cell 1-631-245-9073, email address (marcus.pellow@corvanesupply.com), URL (www.corvanesupply.com

Requirements
Must have
• Must include Business Colors (Black, Green, Blue, White) see sample website file
Nice to have
• emboss, spot uv, etc

```html
<!DOCTYPE html>
<html lang="en">
<head>
<meta charset="utf-8">
<title>Corvane Supply Business Card</title>
<link href="https://fonts.googleapis.com/css2?family=Arimo:wght@400&display=swap" rel="stylesheet">
<style>
  :root {
    --bg: #d4d4d4;
    --white: #ffffff;
    --black: #000000;
    --blue: #0716e0;
    --green: #10e80a;
    --ink: #111111;
  }
  * { margin: 0; padding: 0; box-sizing: border-box; }
  html, body {
    width: 1200px; height: 800px; overflow: hidden;
    background: var(--bg);
    font-family: "Arimo", Arial, sans-serif;
  }
  .stage { position: relative; width: 1200px; height: 800px; }
  .card {
    position: absolute; left: 337px;
    width: 525px; height: 300px;
    border-radius: 20px; overflow: hidden;
    border-bottom: 3px solid var(--blue);
    box-shadow: 0 10px 24px rgba(0,0,0,0.25);
  }
  .card-front { top: 70px; background: var(--white); }
  .card-back { top: 420px; background: var(--black); }

  .holder { position: absolute; left: 38px; top: 46px; }
  .holder-name { font-size: 27px; color: var(--ink); letter-spacing: 0.5px; line-height: 1; }
  .holder-role { font-size: 17px; color: var(--blue); margin-top: 2px; }

  .contact-band {
    position: absolute; left: 0; top: 112px;
    width: 345px; height: 108px;
    background: var(--blue);
    clip-path: polygon(0 0, 100% 0, 88% 100%, 0 100%);
    padding: 12px 0 0 34px;
  }
  .contact-line {
    display: flex; align-items: center; gap: 8px;
    color: var(--white); font-size: 15px; line-height: 21px;
  }
  .contact-line svg { width: 13px; height: 13px; flex: none; }

  .company { position: absolute; left: 38px; top: 234px; }
  .company-name { font-size: 17px; color: var(--blue); }
  .company-address { font-size: 15px; color: var(--ink); margin-top: 4px; }

  .accent-square {
    position: absolute; right: 0; top: 28px;
    width: 62px; height: 74px; background: var(--green);
  }
  .front-mark {
    position: absolute; left: 352px; top: 130px;
    display: flex; align-items: center; gap: 10px;
  }
  .mark-dot { width: 34px; height: 34px; border-radius: 50%; background: var(--blue); flex: none; }
  .front-mark .mark-name { font-size: 22px; color: var(--black); }

  .back-mark {
    position: absolute; inset: 0;
    display: flex; align-items: center; justify-content: center; gap: 16px;
  }
  .back-mark .mark-dot { width: 44px; height: 44px; }
  .back-mark .mark-name { font-size: 38px; color: var(--white); letter-spacing: 1px; }
</style>
</head>
<body>
<main class="stage">
  <section class="card card-front" aria-label="Card front">
    <div class="accent-square"></div>

    <div class="holder">
      <div class="holder-name">MARCUS PELLOW</div>
      <div class="holder-role">President</div>
    </div>

    <div class="contact-band">
      <div class="contact-line">
        <svg viewBox="0 0 16 16" aria-hidden="true"><path fill="#fff" d="M3 1l3 3-2 2c1 2 3 4 5 5l2-2 3 3-2 2C7 14 2 9 1 3z"/></svg>
        1-855-302-4418
      </div>
      <div class="contact-line">
        <svg viewBox="0 0 16 16" aria-hidden="true"><rect x="4" y="1" width="8" height="14" rx="1.5" fill="none" stroke="#fff" stroke-width="1.6"/></svg>
        1-631-245-9073
      </div>
      <div class="contact-line">
        <svg viewBox="0 0 16 16" aria-hidden="true"><rect x="1" y="3" width="14" height="10" fill="#fff"/><path d="M1 3l7 6 7-6" fill="none" stroke="#0716e0" stroke-width="1.4"/></svg>
        marcus.pellow@corvanesupply.com
      </div>
      <div class="contact-line">
        <svg viewBox="0 0 16 16" aria-hidden="true"><circle cx="8" cy="8" r="6.5" fill="none" stroke="#fff" stroke-width="1.4"/><ellipse cx="8" cy="8" rx="3" ry="6.5" fill="none" stroke="#fff" stroke-width="1.2"/><path d="M1.5 8h13" stroke="#fff" stroke-width="1.2"/></svg>
        www.corvanesupply.com
      </div>
    </div>

    <div class="front-mark">
      <span class="mark-dot"></span>
      <span class="mark-name">Corvane Supply</span>
    </div>

    <div class="company">
      <div class="company-name">Corvane Supply Inc</div>
      <div class="company-address">58 Fernhollow Lane, Brentwood NY 11742</div>
    </div>
  </section>

  <section class="card card-back" aria-label="Card back">
    <div class="back-mark">
      <span class="mark-dot"></span>
      <span class="mark-name">CORVANE SUPPLY</span>
    </div>
  </section>
</main>
</body>
</html>
```